Pemberton Dialworks Business Card Design

Double Sided Business Card Design for a Locksmith company specializing in Safecracking, safe & vault service.

```html
<!DOCTYPE html>
<html lang="en">
<head>
<meta charset="utf-8">
<title>Pemberton Dialworks Business Card</title>
<link href="https://fonts.googleapis.com/css2?family=Lato:wght@400;700;900&display=swap" rel="stylesheet">
<style>
  :root{
    --bg:#a3a3a3;
    --card:#ffffff;
    --green:#357e3c;
    --ink:#111111;
    --grey:#555555;
  }
  html,body{margin:0;padding:0;width:1200px;height:1200px;overflow:hidden;background:var(--bg);}
  body{position:relative;font-family:'Lato',sans-serif;}
  .card{position:absolute;left:194px;width:817px;height:469px;background:var(--card);border-radius:38px;overflow:hidden;}
  .card--front{top:100px;}
  .card--back{top:616px;}
  .wordmark{position:absolute;margin:0;font-family:'Lato',sans-serif;font-weight:900;color:var(--ink);text-transform:uppercase;line-height:1;}
  .card--front .wordmark{left:51px;top:50px;font-size:38px;letter-spacing:1px;}
  .card--back .wordmark{left:320px;top:210px;font-size:40px;letter-spacing:1px;}
  .wordmark span{display:block;}
  .wordmark span + span{margin-top:8px;}
  .mark{position:absolute;border-radius:50%;background:var(--green);}
  .card--front .mark{left:436px;top:144px;width:280px;height:280px;}
  .card--back .mark{left:123px;top:148px;width:174px;height:174px;}
  .person{position:absolute;left:51px;top:183px;}
  .person__name{margin:0;font-weight:700;font-size:27px;color:var(--green);line-height:1.1;}
  .person__role{margin:2px 0 0;font-size:19px;color:var(--grey);}
  .address{position:absolute;left:51px;top:258px;margin:0;font-style:normal;font-size:19px;line-height:24px;color:var(--grey);}
  .contacts{position:absolute;left:51px;top:322px;margin:0;padding:0;list-style:none;font-size:19px;color:var(--grey);}
  .contacts li{display:flex;align-items:center;height:24px;}
  .contacts svg{width:14px;height:14px;margin-right:13px;fill:var(--green);flex:none;}
  .website{position:absolute;left:0;right:0;top:398px;margin:0;text-align:center;font-size:19px;font-weight:700;letter-spacing:3.5px;color:var(--grey);}
  .website b{color:var(--green);font-weight:700;}
</style>
</head>
<body>
  <section class="card card--front">
    <h1 class="wordmark"><span>Pemberton</span><span>Dialworks</span></h1>
    <div class="person">
      <p class="person__name">Adrian Kellworth</p>
      <p class="person__role">Co-founder</p>
    </div>
    <address class="address">2048 Halden, Marrow<br>Utca 9-13.</address>
    <ul class="contacts">
      <li><svg viewBox="0 0 24 24"><path d="M6.6 10.8a15 15 0 0 0 6.6 6.6l2.2-2.2c.3-.3.7-.4 1-.2 1.1.4 2.3.6 3.6.6.6 0 1 .4 1 1V20c0 .6-.4 1-1 1A17 17 0 0 1 3 4c0-.6.4-1 1-1h3.5c.6 0 1 .4 1 1 0 1.3.2 2.5.6 3.6.1.3 0 .7-.2 1z"/></svg>+36.1.555.0184</li>
      <li><svg viewBox="0 0 24 24"><path d="M2 9c3-4 17-4 20 0l-2 3-4-1V9H8v2l-4 1zM6 13h12l2 7H4z"/></svg>+36.30.555.0917</li>
      <li><svg viewBox="0 0 24 24"><path d="M2 5h20v14H2zm2 2v1l8 5 8-5V7l-8 5z"/></svg>pembertondialworks@mail.com</li>
      <li><svg viewBox="0 0 24 24"><circle cx="12" cy="12" r="10"/></svg>www.pembertondialworks.com</li>
    </ul>
    <div class="mark" aria-hidden="true"></div>
  </section>

  <section class="card card--back">
    <div class="mark" aria-hidden="true"></div>
    <h2 class="wordmark"><span>Pemberton</span><span>Dialworks</span></h2>
    <p class="website">www.<b>pembertondialworks</b>.com</p>
  </section>
</body>
</html>
```